Bref créative
Stationery for bright harbor company
Stationery for my company
Professional
Farhan Tariq Baloch
General Manager
Prince Faisal Street,
Al Warood,
Riyadh,
Saudi Arabia.
P.O.Box:5831-6-40921-3158.
farhan@br1ghth4rb0r.example
www.br1ghth4rb0r.example
C.R.
I want something creative, plus if it is possible can you put the information editable so I can put the other names and titles for the other co - workers
My logo or something creative
logo to be used
like this

```html
<!DOCTYPE html>
<html lang="en">
<head>
<meta charset="utf-8">
<title>Bright Harbor Company – Business Card</title>
<link href="https://fonts.googleapis.com/css2?family=PT+Sans:wght@400;700&display=swap" rel="stylesheet">
<style>
  :root {
    --page-bg: #e9e6e1;
    --card-bg: #ffffff;
    --brand-blue: #1f6f98;
    --brand-blue-dark: #0f4663;
    --brand-blue-light: #4f9cc3;
    --ink-dark: #2b2f33;
    --ink-mid: #5f6468;
    --rule: #c9cdd0;
  }
  * { margin: 0; padding: 0; box-sizing: border-box; }
  html, body {
    width: 1200px; height: 780px; overflow: hidden;
    background: var(--page-bg);
    font-family: "PT Sans", Arial, sans-serif;
  }
  .canvas {
    position: relative; width: 1200px; height: 780px;
    display: flex; align-items: center; justify-content: center;
  }
  .business-card {
    position: relative; width: 960px; height: 540px;
    background: var(--card-bg);
    border-radius: 10px 40px 40px 10px;
    box-shadow: 0 12px 30px rgba(0,0,0,0.18);
    overflow: hidden;
  }
  .edge-band {
    position: absolute; left: 0; top: 0; bottom: 0; width: 34px;
    background: linear-gradient(90deg, var(--brand-blue-dark), var(--brand-blue) 55%, var(--brand-blue-light));
  }
  .edge-band::after {
    content: ""; position: absolute; right: 6px; top: 0; bottom: 0;
    width: 3px; background: rgba(255,255,255,0.85);
  }
  .brand-block {
    position: absolute; left: 60px; top: 0; width: 290px; height: 100%;
    display: flex; flex-direction: column; align-items: center; justify-content: center;
    gap: 18px;
  }
  .brand-dot {
    width: 120px; height: 120px; border-radius: 50%;
    background: var(--brand-blue);
  }
  .brand-name {
    font-weight: 700; font-size: 40px; color: var(--brand-blue-dark);
    letter-spacing: 0.5px;
  }
  .divider {
    position: absolute; left: 370px; top: 50px; bottom: 50px;
    width: 1px; background: var(--rule);
  }
  .contact-block {
    position: absolute; left: 405px; top: 48px; right: 40px;
    color: var(--ink-mid);
  }
  .person-name {
    font-weight: 700; font-size: 32px; color: var(--brand-blue);
    line-height: 1.1;
  }
  .person-title {
    font-size: 20px; color: var(--ink-mid); margin-top: 8px;
  }
  .address {
    font-size: 20px; line-height: 1.35; margin-top: 48px; color: var(--ink-mid);
  }
  .contact-list {
    list-style: none; margin-top: 34px;
  }
  .contact-list li {
    display: flex; align-items: center; gap: 12px;
    font-size: 20px; line-height: 1.5; color: var(--ink-dark);
  }
  .contact-list svg {
    width: 20px; height: 20px; flex: none;
    fill: none; stroke: var(--ink-mid); stroke-width: 2; stroke-linecap: round; stroke-linejoin: round;
  }
</style>
</head>
<body>
<main class="canvas">
  <article class="business-card">
    <div class="edge-band"></div>

    <section class="brand-block">
      <div class="brand-dot"></div>
      <div class="brand-name">Brightharbor</div>
    </section>

    <div class="divider"></div>

    <section class="contact-block">
      <h1 class="person-name">Farhan Tariq Baloch</h1>
      <p class="person-title">General Manager</p>

      <p class="address">
        Prince Faisal Street, Al Warood,<br>
        Riyadh, Saudi Arabia.<br>
        P.O.Box:5831-6-40921-3158
      </p>

      <ul class="contact-list">
        <li>
          <svg viewBox="0 0 24 24"><path d="M5 3h4l2 5-3 2a11 11 0 0 0 6 6l2-3 5 2v4a2 2 0 0 1-2 2A17 17 0 0 1 3 5a2 2 0 0 1 2-2z"/></svg>
          (+966) (01) 5550142
        </li>
        <li>
          <svg viewBox="0 0 24 24"><rect x="7" y="2" width="10" height="20" rx="2"/><line x1="11" y1="18" x2="13" y2="18"/></svg>
          (+966) 555012873
        </li>
        <li>
          <svg viewBox="0 0 24 24"><rect x="7" y="3" width="10" height="7"/><rect x="4" y="10" width="16" height="9" rx="1"/><line x1="8" y1="14" x2="16" y2="14"/></svg>
          (+966) (01) 5550143
        </li>
        <li>
          <svg viewBox="0 0 24 24"><circle cx="12" cy="12" r="4"/><path d="M16 8v5a3 3 0 0 0 6 0v-1a10 10 0 1 0-4 8"/></svg>
          farhan@br1ghth4rb0r.example
        </li>
        <li>
          <svg viewBox="0 0 24 24"><circle cx="12" cy="12" r="9"/><line x1="3" y1="12" x2="21" y2="12"/><path d="M12 3a14 14 0 0 1 0 18a14 14 0 0 1 0-18"/></svg>
          www.br1ghth4rb0r.example
        </li>
      </ul>
    </section>
  </article>
</main>
</body>
</html>
```